Velvet Harbor Gentlemen's Club 20 YR Anniversary

Need artwork for:
9.65 inches (wide) x 5.34 inches (high) [newspaper ad]
Facebook Cover Photo
Facebook Profile Picture
The design should be consistent throughout the different sizes.

The document attached has the party information.

The party is for our 20 yr anniversary but the highlight of the event is FREE LAP DANCES FOR EVERYBODY
We'd like to use the colors black, red and gold but we are open to any artists thoughts and ideas.

I tried to attach a photo of the guest performer. But when I tried to upload it I received this message: Sorry, you can only upload files up to 4096px in width. At 5616px the file 'IMG_6454edit.jpg' is too wide. I've attached an alternate photo. I hope we can one of them.

Colors
fbed22
ec1f27

Requirements
Must have
• VHG logo
• FREE LAP DANCES FOR EVERYBODY
• No Gimmicks, No Catch...No Strings Attached

```html
<!DOCTYPE html>
<html lang="en">
<head>
<meta charset="utf-8">
<title>Velvet Harbor Gentlemen's Club – 20 Year Anniversary</title>
<link href="https://fonts.googleapis.com/css2?family=Monoton&family=Montserrat:wght@800;900&family=Oswald:wght@300;500;700&family=Roboto+Condensed:ital,wght@0,700;1,400&display=swap" rel="stylesheet">
<style>
  :root {
    --red: #ec1f27;
    --red-deep: #a5141a;
    --red-dark: #7d0e12;
    --gold: #fbed22;
    --gold-warm: #f6c51f;
    --white: #ffffff;
    --ink: #111111;
    --plum: #6b2a5a;
  }
  * { margin: 0; padding: 0; box-sizing: border-box; }
  html, body { width: 1200px; height: 665px; overflow: hidden; background: var(--white); }
  .ad {
    position: relative;
    width: 1200px;
    height: 665px;
    overflow: hidden;
    background: radial-gradient(ellipse at 55% 40%, var(--red) 0%, #c81a20 45%, var(--red-deep) 80%, var(--red-dark) 100%);
  }
  .anniversary { position: absolute; left: 0; top: 0; width: 1200px; height: 60px; }
  .anniversary text {
    font-family: "Montserrat", sans-serif;
    font-weight: 900;
    font-size: 27px;
    fill: var(--white);
  }
  .headline { position: absolute; left: 0; top: 0; width: 1200px; height: 320px; }
  .headline text { font-family: "Monoton", sans-serif; fill: var(--gold); }
  .headline .for { font-family: "Oswald", sans-serif; font-weight: 700; fill: var(--gold-warm); }
  .no-catch {
    position: absolute;
    left: 906px; top: 190px;
    font-family: "Roboto Condensed", sans-serif;
    font-weight: 700;
    font-size: 20px;
    line-height: 23px;
    letter-spacing: 1px;
    color: var(--gold);
    text-transform: uppercase;
    white-space: nowrap;
  }
  .performer-photo {
    position: absolute;
    left: 290px; top: 232px;
    width: 770px; height: 344px;
    background: radial-gradient(ellipse at 62% 55%, var(--plum) 0%, #7b2848 45%, rgba(160,24,34,0) 78%);
  }
  .details { position: absolute; left: 40px; top: 400px; white-space: nowrap; }
  .details .catering {
    font-family: "Oswald", sans-serif; font-weight: 300;
    font-size: 22px; color: var(--gold); letter-spacing: 0.5px; text-transform: uppercase;
  }
  .details .drinks {
    font-family: "Montserrat", sans-serif; font-weight: 900;
    font-size: 30px; color: var(--white); letter-spacing: 2px; margin-top: 0;
  }
  .details .shows {
    font-family: "Oswald", sans-serif; font-weight: 300;
    font-size: 22px; color: var(--gold); text-transform: uppercase; margin-top: 0;
  }
  .headliner { display: flex; align-items: center; gap: 10px; }
  .headliner .name {
    font-family: "Montserrat", sans-serif; font-weight: 900;
    font-size: 40px; color: var(--white); letter-spacing: 1px;
  }
  .headliner .when {
    font-family: "Oswald", sans-serif; font-weight: 500;
    font-size: 15px; line-height: 17px; color: var(--gold); text-transform: uppercase;
  }
  .contact-band {
    position: absolute; left: 0; top: 576px;
    width: 1200px; height: 89px; background: var(--white);
  }
  .contact { position: absolute; left: 40px; top: 6px; white-space: nowrap; }
  .contact .phone {
    font-family: "Roboto Condensed", sans-serif; font-weight: 700;
    font-size: 30px; color: var(--red); letter-spacing: 1px;
  }
  .contact .line {
    font-family: "Roboto Condensed", sans-serif; font-style: italic; font-weight: 400;
    font-size: 17px; color: var(--ink); letter-spacing: 0.5px; line-height: 23px;
  }
  .contact .line span + span { margin-left: 22px; }
  .brand {
    position: absolute; right: 24px; top: 8px;
    display: flex; align-items: center; gap: 10px;
  }
  .brand .mark { width: 14px; height: 14px; background: var(--ink); border-radius: 50%; }
  .brand .name {
    font-family: "Montserrat", sans-serif; font-weight: 900;
    font-size: 56px; color: var(--ink); letter-spacing: 1px;
  }
</style>
</head>
<body>
<main class="ad">
  <div class="performer-photo" role="img" aria-label="Photo of the guest performer reclining on a purple tufted wingback chair"></div>

  <svg class="anniversary" viewBox="0 0 1200 60" aria-label="Celebrating Velvet Harbor Gentlemen's Club 20YR Anniversary">
    <text x="40" y="46" textLength="1040" lengthAdjust="spacingAndGlyphs">CELEBRATING VELVET HARBOR GENTLEMEN'S CLUB  20YR ANNIVERSARY</text>
  </svg>

  <svg class="headline" viewBox="0 0 1200 320" aria-label="Free lapdances for everybody!">
    <text x="42" y="178" font-size="128" textLength="1116" lengthAdjust="spacingAndGlyphs">FREE LAPDANCES</text>
    <text class="for" x="44" y="214" font-size="24">F</text>
    <text class="for" x="44" y="246" font-size="24">O</text>
    <text class="for" x="45" y="278" font-size="24">R</text>
    <text x="68" y="292" font-size="120" textLength="830" lengthAdjust="spacingAndGlyphs">EVERYBODY!</text>
  </svg>

  <p class="no-catch">No gimmicks…<br>No catch…<br>No strings attached!</p>

  <section class="details">
    <p class="catering">Catered dinner by Marino's Trattoria until 10pm</p>
    <p class="drinks">$3.50 DRINKS ALL NIGHT</p>
    <p class="shows">Featuring 3 shows with 2015 Miss Nude Midwest</p>
    <div class="headliner">
      <span class="name">SCARLET VANE</span>
      <span class="when">On Thursday May 12<br>From 6pm until…</span>
    </div>
  </section>

  <footer class="contact-band">
    <div class="contact">
      <p class="phone">414-555-0188</p>
      <p class="line">4820 South Harbor Ave. &nbsp;Bayview, WI</p>
      <p class="line"><span>WWW.VHG.CLUB</span><span>FB/CLUBVHGWI</span></p>
    </div>
    <div class="brand">
      <span class="mark"></span>
      <span class="name">VHG</span>
    </div>
  </footer>
</main>
</body>
</html>
```